Contractor Business Card Design

Looking to have a card made that has a bold description of (KITCHENS, BASEMENTS, BATHROOMS)

Definition and layers a plus

Contact info is;

Mark T. Ellery
Larkfield, MN 55990
Cell: 612-555-0147
website: www.cobaltfinishworks.example
Email: cobaltfinishworksmn@mailbox.example

colors: red, black, gray, white

Contact Information for Business Card

Contact info is;

Mark T. Ellery
Larkfield, MN 55990
Cell: 612-555-0147

Colors
ec1f27

Requirements
Must have
• Looking for layers and definition
Nice to have
• Cards are planned to be printed on plastic cards

```html
<!DOCTYPE html>
<html lang="en">
<head>
<meta charset="utf-8">
<title>Cobalt Finishworks – Business Card</title>
<link rel="stylesheet" href="https://fonts.googleapis.com/css2?family=Montserrat:wght@600;700&family=Arimo:wght@400&display=swap">
<style>
  :root {
    --stage: #0e0e0f;
    --card: #2a2a2c;
    --card-edge: #ec1f27;
    --red: #ec1f27;
    --white: #f4f4f4;
    --gray: #b4b4b6;
    --gray-dim: #8a8a8d;
    --rule: #5a5a5d;
  }
  * { box-sizing: border-box; margin: 0; padding: 0; }
  html, body { width: 1200px; height: 820px; overflow: hidden; background: var(--stage); }
  .sheet {
    width: 1200px; height: 820px;
    display: flex; flex-direction: column; align-items: center; justify-content: center; gap: 36px;
  }
  .card {
    position: relative;
    width: 650px; height: 370px;
    background: var(--card);
    border: 2px solid var(--card-edge);
    border-radius: 4px;
    font-family: "Arimo", Arial, sans-serif;
    overflow: hidden;
  }

  /* Front */
  .brand {
    position: absolute; left: 190px; top: 70px;
    display: flex; align-items: center; gap: 18px;
  }
  .brand-mark {
    width: 78px; height: 78px; border-radius: 50%;
    border: 4px solid var(--white);
  }
  .brand-name {
    font-family: "Montserrat", Arial, sans-serif; font-weight: 700;
    font-size: 30px; letter-spacing: 1px; color: var(--white);
    text-transform: uppercase; line-height: 1.05;
  }
  .name-row {
    position: absolute; left: 40px; right: 40px; top: 190px;
    display: flex; align-items: center; gap: 16px;
  }
  .holder {
    flex: none;
    font-family: "Montserrat", Arial, sans-serif; font-weight: 700;
    font-size: 22px; line-height: 1.2; color: var(--red);
    text-transform: uppercase; letter-spacing: 0.5px;
  }
  .divider { flex: 1; border-top: 1px solid var(--rule); }
  .contact-list {
    position: absolute; left: 40px; top: 240px;
    list-style: none; display: flex; flex-direction: column; gap: 7px;
    font-size: 17px; color: var(--gray);
  }
  .contact-list li { display: flex; align-items: center; gap: 10px; white-space: nowrap; }
  .contact-list svg { width: 17px; height: 17px; flex: none; }
  .address {
    position: absolute; right: 40px; top: 248px;
    font-size: 18px; color: var(--gray-dim); white-space: nowrap;
  }

  /* Back */
  .services { position: absolute; left: 40px; top: 30px; right: 36px; }
  .service { margin-bottom: 12px; }
  .service h2 {
    font-family: "Arimo", Arial, sans-serif; font-weight: 400;
    font-size: 17px; color: var(--red); text-transform: uppercase; line-height: 1.25;
  }
  .service p { font-size: 14.5px; line-height: 1.32; color: var(--white); }
</style>
</head>
<body>
<main class="sheet">

  <section class="card card-front" aria-label="Business card front">
    <div class="brand">
      <span class="brand-mark" aria-hidden="true"></span>
      <span class="brand-name">Cobalt<br>Finishworks</span>
    </div>
    <div class="name-row">
      <h1 class="holder">Mark T. Ellery</h1>
      <span class="divider" aria-hidden="true"></span>
    </div>
    <ul class="contact-list">
      <li>
        <svg viewBox="0 0 24 24" aria-hidden="true"><path fill="#ec1f27" d="M6.6 10.8a15 15 0 0 0 6.6 6.6l2.2-2.2c.3-.3.7-.4 1-.2 1.1.4 2.3.6 3.6.6.6 0 1 .4 1 1V20c0 .6-.4 1-1 1A17 17 0 0 1 3 4c0-.6.4-1 1-1h3.5c.6 0 1 .4 1 1 0 1.2.2 2.4.6 3.6.1.3 0 .7-.2 1z"/></svg>
        612-555-0147
      </li>
      <li>
        <svg viewBox="0 0 24 24" aria-hidden="true"><g fill="none" stroke="#ec1f27" stroke-width="2"><circle cx="12" cy="12" r="9"/><path d="M3 12h18M12 3c3 3 3 15 0 18M12 3c-3 3-3 15 0 18"/></g></svg>
        www.cobaltfinishworks.example
      </li>
      <li>
        <svg viewBox="0 0 24 24" aria-hidden="true"><rect x="2" y="5" width="20" height="14" fill="#ec1f27"/><path d="M2 5l10 8 10-8" fill="none" stroke="#2a2a2c" stroke-width="1.6"/></svg>
        cobaltfinishworksmn@mailbox.example
      </li>
    </ul>
    <p class="address">Larkfield, MN 55990</p>
  </section>

  <section class="card card-back" aria-label="Business card back">
    <div class="services">
      <article class="service">
        <h2>Kitchens</h2>
        <p>The main functions of a kitchen are to store, prepare and cook food.<br>
        The room or area may also be used for dining,<br>
        entertaining and laundry.<br>
        The design and construction of kitchens is a huge market<br>
        all over the world.</p>
      </article>
      <article class="service">
        <h2>Basements</h2>
        <p>A basement is a room that's below ground level<br>
        underneath the first floor.<br>
        Some basements are "finished," with carpeting<br>
        and solid ceilings and walls.</p>
      </article>
      <article class="service">
        <h2>Bathrooms</h2>
        <p>A bathroom is a room for personal hygiene activities generally<br>
        containing a toilet, a sink and either a bathtub a shower, or both.</p>
      </article>
    </div>
  </section>

</main>
</body>
</html>
```